mykelvoratrim needs a package design

myKelvoraTrim - a individual micronutrient product for sporty people. We want to sell individual micronutrients to / for high performance sportsmen. (Granules.jpg eg.) The recipes are based on our customer's answers in a questionnaire. As the name of our product myKelvoraTrim tells, our target audience are healthy sportsmen aged in between 30 to 60 years with a higher level of income. We already have a logo, now we need a design for our cans. The size of the can-area is 245x180mm a 3mm border. Consider the attachement. The logo has to be on the design. Additionally a 70x45mm clean space needs to be on it, we will stick a transparent label with personalData of our customers on it. (Eg. "Hobbs mixture") The fontcolour will be black for the customers dataonly. The label printer doze support colors. You may add a name and a slight border in the design, so we can imagine how it looks better on the can. The font used for the logo is "Good Times".

Industry/Entity Type

Product

Font styles to use
Serif
Sans Serif

Requirements
Should not have
• We do not need any information about content on the can (magnesium ...), this will be on the package insert.

```html
<!DOCTYPE html>
<html lang="en">
<head>
<meta charset="utf-8">
<title>myKelvoraTrim – Can Wrap</title>
<link rel="stylesheet" href="https://fonts.googleapis.com/css2?family=Exo+2:wght@500&display=swap">
<style>
  :root {
    --stage: #e9e9ea;
    --wrap-top: #aab4c9;
    --wrap-mid: #c9d2e2;
    --wrap-low: #e4e6ea;
    --title-blue: #1d62a3;
    --name-grey: #4f555e;
    --runner-deep: #6f82bd;
    --runner-light: #a9c9e3;
    --label-fill: rgba(226, 232, 243, 0.75);
    --label-edge: rgba(255, 255, 255, 0.55);
  }
  * { margin: 0; padding: 0; box-sizing: border-box; }
  html, body { width: 1200px; height: 1200px; overflow: hidden; background: var(--stage); }
  .canvas { position: relative; width: 1200px; height: 1200px; }

  .can-wrap {
    position: absolute; left: 50px; top: 196px; width: 1100px; height: 808px;
    background:
      linear-gradient(180deg, rgba(0,0,0,0) 55%, var(--wrap-low) 100%),
      linear-gradient(90deg, var(--wrap-top) 0%, var(--wrap-mid) 25%, var(--wrap-top) 50%, var(--wrap-mid) 75%, var(--wrap-top) 100%);
    overflow: hidden;
    font-family: "Exo 2", sans-serif;
    font-weight: 500;
  }
  .panel { position: absolute; top: 0; width: 550px; height: 808px; }
  .panel--front { left: 0; }
  .panel--back { left: 550px; }

  .brand-name {
    position: absolute; left: 0; width: 100%;
    display: flex; align-items: center; justify-content: center; gap: 10px;
    color: var(--name-grey); font-size: 24px; line-height: 1.2;
  }
  .brand-name__dot {
    width: 10px; height: 10px; border-radius: 50%; background: var(--name-grey);
  }
  .panel--front .brand-name { top: 138px; }
  .panel--back .brand-name { top: 700px; font-size: 22px; }

  .product-title { position: absolute; top: 352px; left: 0; width: 100%; text-align: center; color: var(--title-blue); }
  .product-title__kicker { font-size: 14px; letter-spacing: 1px; margin-bottom: 4px; }
  .product-title__main { font-size: 44px; line-height: 1; letter-spacing: 1px; }

  .runner-illustration {
    position: absolute; left: 0; top: 470px; width: 550px; height: 338px;
    background: radial-gradient(ellipse at 30% 60%, var(--runner-deep) 0%, rgba(111,130,189,0.7) 35%, rgba(169,201,227,0.5) 60%, rgba(169,201,227,0) 80%);
  }
  .particle-spray {
    position: absolute; left: 0; top: 470px; width: 320px; height: 210px;
    background: radial-gradient(ellipse at 25% 50%, rgba(120,180,220,0.55) 0%, rgba(169,201,227,0.3) 50%, rgba(169,201,227,0) 80%);
  }
  .personal-label-area {
    position: absolute; left: 45px; top: 40px; width: 460px; height: 420px;
    background: var(--label-fill); border: 2px solid var(--label-edge);
  }
</style>
</head>
<body>
<div class="canvas">
  <div class="can-wrap">
    <section class="panel panel--front">
      <div class="brand-name"><span class="brand-name__dot"></span>myKelvoraTrim</div>
      <div class="product-title">
        <div class="product-title__kicker">HIGH PERFORMANCE</div>
        <div class="product-title__main">MICRO<br>NUTRIENTS</div>
      </div>
      <div class="runner-illustration" role="img" aria-label="Watercolour silhouette of a running athlete dissolving into blue particles"></div>
    </section>
    <section class="panel panel--back">
      <div class="personal-label-area" aria-label="Clean space for the personalised transparent customer label"></div>
      <div class="particle-spray" role="img" aria-label="Scattered blue watercolour particles"></div>
      <div class="brand-name"><span class="brand-name__dot"></span>myKelvoraTrim</div>
    </section>
  </div>
</div>
</body>
</html>
```